KE Mall

I need a powerful power point presentation to translate my executive summary into words and graphics, utilizing all the resources necessary to produce a 12-14 page Powerpoint pitch book in order to convince potential investors of my business idea. The concept behind the Mall is to develop a number of unique standalone community malls, targeting the under-served residential communities in -.
The Mall will be built around family and their younger generation audience, creating a unique atmosphere that is conducive to making the MALL a regular local destination for the residents.
Each community mall will be remarkably designed around light, nature and music in a way not done before. The Mall will bring essential goods and services to each community that has been neglected by the large mall operators. [PLEASE CHECK ATTACHMENT OF THE PITCH BOOK WHICH I DREW OUT TO GIVE YOU AN IDEA OF THE ESSENTIAL PAGES]
Updates

I have added the LOGO of the project to give you an idea of how to choose your color schemes for the powerpoint presentation.

Reason: Interesting submissions. Need more time to assess with designers..

Dear all,

I am on the verge of finalizing with a designer. Anyone who has or about to start working on a design, I would ask you not to in order not to waste your time. Many thanks for your interests..

Target Market(s)

Mid to upper market. Colours should be greys, blacks, browns and earthy.. This is a mall project in the middle of the desert.

Industry/Entity Type

Residential

Requirements
Must have
• Since this is a real estate project, there must be maps of the area surrounding the project, the actual location using google maps, nice soft rounded/friendly graphics showing returns to investors and cost of project, snap shots of mall designs that give an idea of the design (actual designs will be given later)... Etc..
Nice to have
• Cool graphics, info graphics explaining things in a way investors can grab, especially relating to financial matters. Ha to have a good sense of continuity in the presentation..
Should not have
• too bright or fun colours... This is a serious real estate project BUT it is designed for the younger generation but for the enjoyment of all. The only bright colours will come from the logo which is under design. The logo will have an element of orange and red in it.

```html
<!DOCTYPE html>
<html lang="en">
<head>
<meta charset="utf-8">
<title>KE Mall — Executive Summary</title>
<link href="https://fonts.googleapis.com/css2?family=Open+Sans:wght@400;600;700&family=Arimo:wght@400&family=Roboto+Condensed:wght@700&display=swap" rel="stylesheet">
<style>
  :root {
    --brand-brown: #a45e02;
    --brand-brown-text: #a5600a;
    --white: #ffffff;
    --page-bg: #ffffff;
    --footer-light: #ffffff;
    --footer-mid: #e9e9e9;
    --footer-dark: #c9c9c9;
    --pattern-tone: #ececec;
  }
  * { margin: 0; padding: 0; box-sizing: border-box; }
  html, body { width: 1200px; height: 900px; overflow: hidden; background: var(--page-bg); }
  .slide { position: relative; width: 1200px; height: 900px; overflow: hidden; background: var(--page-bg); }

  .header-band {
    position: absolute; left: 0; top: 0; width: 1200px; height: 342px;
    background: var(--brand-brown);
  }
  .slide-title {
    position: absolute; left: 92px; top: 254px;
    font-family: "Open Sans", sans-serif; font-weight: 700; font-size: 68px;
    letter-spacing: 0.5px; color: var(--white); line-height: 1;
    text-shadow: 0 2px 3px rgba(0,0,0,0.35);
  }
  .slide-subtitle {
    position: absolute; right: 34px; top: 292px;
    font-family: "Arimo", sans-serif; font-size: 25px; color: var(--white); line-height: 1;
  }

  .backdrop-pattern {
    position: absolute; left: 540px; top: 342px; width: 660px; height: 478px;
    background: radial-gradient(ellipse at 70% 20%, var(--pattern-tone) 0%, rgba(236,236,236,0.5) 40%, rgba(255,255,255,0) 75%);
  }

  .topic-row { position: absolute; left: 0; top: 431px; width: 1200px; height: 240px; }
  .topic { position: absolute; top: 0; width: 240px; height: 240px; }
  .topic svg { position: absolute; inset: 0; }
  .topic-label {
    position: absolute; inset: 0; display: flex; align-items: center; justify-content: center;
    text-align: center; font-family: "Open Sans", sans-serif; font-weight: 600;
    font-size: 34px; line-height: 47px; color: var(--white);
    text-shadow: 0 1px 2px rgba(0,0,0,0.35);
  }
  .topic--company { left: 59px; }
  .topic--market { left: 346px; }
  .topic--financial { left: 633px; }
  .topic--structure { left: 920px; }

  .footer-rule {
    position: absolute; left: 0; top: 819px; width: 1200px; height: 3px; background: var(--brand-brown);
  }
  .footer-band {
    position: absolute; left: 0; top: 825px; width: 1200px; height: 75px;
    background: linear-gradient(to bottom, var(--footer-light) 0%, var(--footer-mid) 45%, var(--footer-dark) 100%);
  }
  .footer-text {
    position: absolute; right: 18px; top: 848px;
    font-family: "Roboto Condensed", sans-serif; font-weight: 700; font-size: 27px;
    color: var(--brand-brown-text); line-height: 1;
  }
</style>
</head>
<body>
<div class="slide">
  <div class="header-band"></div>
  <h1 class="slide-title">KE MALL</h1>
  <p class="slide-subtitle">Executive Summary</p>

  <div class="backdrop-pattern" role="img" aria-label="Faint grey halftone dot pattern in the background"></div>

  <div class="topic-row">
    <div class="topic topic--company">
      <svg width="240" height="240" viewBox="0 0 240 240" aria-hidden="true">
        <defs>
          <linearGradient id="fillCompany" x1="0" y1="0" x2="0" y2="1">
            <stop offset="0" stop-color="#c9a27a"/><stop offset="1" stop-color="#8f6a45"/>
          </linearGradient>
        </defs>
        <circle cx="120" cy="120" r="119" fill="#7d5b3a"/>
        <circle cx="120" cy="120" r="115" fill="url(#fillCompany)"/>
        <ellipse cx="120" cy="42" rx="80" ry="30" fill="#ffffff" opacity="0.16"/>
      </svg>
      <div class="topic-label">Company<br>Description</div>
    </div>

    <div class="topic topic--market">
      <svg width="240" height="240" viewBox="0 0 240 240" aria-hidden="true">
        <defs>
          <linearGradient id="fillMarket" x1="0" y1="0" x2="0" y2="1">
            <stop offset="0" stop-color="#8a5a2b"/><stop offset="1" stop-color="#4e2f14"/>
          </linearGradient>
        </defs>
        <circle cx="120" cy="120" r="119" fill="#43290f"/>
        <circle cx="120" cy="120" r="115" fill="url(#fillMarket)"/>
        <ellipse cx="120" cy="42" rx="80" ry="30" fill="#ffffff" opacity="0.13"/>
      </svg>
      <div class="topic-label">Market<br>Opportunity</div>
    </div>

    <div class="topic topic--financial">
      <svg width="240" height="240" viewBox="0 0 240 240" aria-hidden="true">
        <defs>
          <linearGradient id="fillFinancial" x1="0" y1="0" x2="0" y2="1">
            <stop offset="0" stop-color="#e07d0e"/><stop offset="1" stop-color="#f2b530"/>
          </linearGradient>
        </defs>
        <circle cx="120" cy="120" r="119" fill="#c86e08"/>
        <circle cx="120" cy="120" r="115" fill="url(#fillFinancial)"/>
        <ellipse cx="120" cy="42" rx="80" ry="30" fill="#ffffff" opacity="0.18"/>
      </svg>
      <div class="topic-label">Financial<br>Summary</div>
    </div>

    <div class="topic topic--structure">
      <svg width="240" height="240" viewBox="0 0 240 240" aria-hidden="true">
        <defs>
          <linearGradient id="fillStructure" x1="0" y1="0" x2="0" y2="1">
            <stop offset="0" stop-color="#2a2a2a"/><stop offset="1" stop-color="#4a4a4a"/>
          </linearGradient>
        </defs>
        <circle cx="120" cy="120" r="119" fill="#1a1a1a"/>
        <circle cx="120" cy="120" r="115" fill="url(#fillStructure)"/>
        <ellipse cx="120" cy="42" rx="80" ry="30" fill="#ffffff" opacity="0.08"/>
      </svg>
      <div class="topic-label">Structure</div>
    </div>
  </div>

  <div class="footer-rule"></div>
  <div class="footer-band"></div>
  <p class="footer-text">Footer text here</p>
</div>
</body>
</html>
```